Cold brew coffee concept

Web site/logo for cold brew coffee served in a keg tap. Cold brew coffee is a natural energy beverage roasted with fair trade/organic beans. Based in New England. Think- Fresh, Natural, Organic, Pure, Mills, Brick, Wood. Ferncastle Coldbrew.

Target Market(s)

Individuals looking for energy drinks without added sugar or dairy. Coffee connoisseurs.

Industry/Entity Type

Trade

Logo Text

Ferncastle Coldbrew

Number of Pages Required

1 page

Font styles to use
Serif

```html
<!DOCTYPE html>
<html lang="en">
<head>
<meta charset="utf-8">
<title>Ferncastle Coldbrew</title>
<link href="https://fonts.googleapis.com/css2?family=Great+Vibes&family=Lato:wght@400;700&family=Raleway:wght@400;500&display=swap" rel="stylesheet">
<style>
:root{
  --black:#050403;
  --wood:#1e140d;
  --wood-dark:#120c08;
  --gold:#c9a06a;
  --gold-soft:#b88e5a;
  --cream:#efe6da;
  --text:#d9cfc2;
}
*{margin:0;padding:0;box-sizing:border-box}
html,body{width:873px;height:1200px;overflow:hidden;background:var(--black)}
body{position:relative;font-family:'Lato',sans-serif;color:var(--text)}
.abs{position:absolute}
.topbar{left:0;top:0;width:873px;height:50px;background:var(--black)}
.phone{left:120px;top:14px;display:flex;align-items:center;gap:8px;font-family:'Raleway',sans-serif;font-size:10px;color:var(--cream)}
.phone-icon{width:18px;height:18px;border:1px solid var(--gold);border-radius:50%;display:flex;align-items:center;justify-content:center}
.follow{left:600px;top:13px;display:flex;align-items:center;gap:6px}
.follow-label{font-family:'Great Vibes',cursive;font-size:16px;color:var(--cream);margin-right:4px}
.social{width:18px;height:18px;border:1px solid var(--gold);border-radius:50%}
.navbar{left:0;top:49px;width:873px;height:37px;border-top:1px solid var(--gold-soft);border-bottom:1px solid var(--gold-soft);background:var(--black)}
.nav-item{top:0;height:35px;line-height:35px;font-family:'Raleway',sans-serif;font-size:9.5px;color:var(--cream);transform:translateX(-50%);white-space:nowrap}
.nav-item.active{background:var(--gold);padding:0 10px;transform:none}
.nav-dot{top:16px;width:4px;height:4px;border-radius:50%;background:#666}
.logo{left:386px;top:14px;width:106px;height:106px;border-radius:50%;background:var(--black);border:2px solid var(--gold);display:flex;flex-direction:column;align-items:center;justify-content:center;z-index:5}
.logo-name{font-family:'Raleway',sans-serif;font-size:11px;font-weight:500;color:var(--cream);text-align:center;line-height:1.25}
.logo-mark{width:8px;height:8px;border-radius:50%;background:var(--gold);margin-bottom:6px}
.hero{left:0;top:86px;width:873px;height:444px;
  background:
    radial-gradient(ellipse 110px 150px at 580px 330px,rgba(140,90,45,.95) 0%,rgba(110,70,35,.7) 45%,rgba(0,0,0,0) 100%),
    radial-gradient(ellipse 260px 220px at 600px 120px,rgba(120,118,112,.55) 0%,rgba(0,0,0,0) 100%),
    radial-gradient(ellipse 300px 200px at 330px 230px,rgba(150,110,80,.55) 0%,rgba(0,0,0,0) 100%),
    linear-gradient(90deg,#1f5a3c 0%,#1d4a33 18%,#3a3029 40%,#4a3c30 60%,#2a2622 82%,#1a1816 100%);}
.hero-welcome{left:232px;top:172px;font-family:'Great Vibes',cursive;font-size:28px;color:var(--cream)}
.hero-title{left:156px;top:204px;font-family:'Great Vibes',cursive;font-size:46px;color:var(--gold)}
.arrow{top:265px}
.features{left:0;top:530px;width:873px;height:170px;background:linear-gradient(180deg,#0a0705,var(--wood) 60%,#2a1d13);border-top:1px solid var(--gold-soft)}
.feature{width:230px;transform:translateX(-50%);text-align:center;top:0}
.feature-badge{width:96px;height:96px;margin:-33px auto 0;border-radius:50%;background:var(--black);border-bottom:2px solid var(--gold-soft);display:flex;align-items:center;justify-content:center}
.feature h3{font-family:'Raleway',sans-serif;font-weight:400;font-size:17px;color:var(--gold);margin-top:9px}
.feature p{font-size:9px;line-height:14px;color:var(--cream);font-weight:700;margin-top:6px}
.about{left:0;top:700px;width:873px;height:210px;background:linear-gradient(180deg,#2a1d13,var(--wood) 50%,var(--wood-dark));border-top:1px dashed #4a3726}
.section-title{font-family:'Raleway',sans-serif;font-weight:400;font-size:17px;color:var(--cream)}
.section-title span{color:var(--gold)}
.rule{height:4px;width:14px;border-radius:2px;background:var(--gold-soft)}
.about-text{left:118px;top:62px;width:376px;font-size:8.4px;line-height:16.5px;color:var(--text)}
.read-more{left:128px;top:168px;width:66px;height:22px;border:1.5px solid var(--gold);border-top:none;font-size:8.5px;color:var(--gold);text-align:center;line-height:22px}
.about-photo{left:528px;top:26px;width:224px;height:154px;border:3px solid var(--gold-soft);
  background:
    radial-gradient(ellipse 60px 50px at 85px 60px,rgba(215,215,210,.6) 0%,rgba(0,0,0,0) 100%),
    radial-gradient(ellipse 90px 40px at 150px 125px,rgba(160,100,50,.8) 0%,rgba(0,0,0,0) 100%),
    linear-gradient(180deg,#3c3a35 0%,#56544d 35%,#2a2420 70%,#4a3222 100%);}
.benefits{left:0;top:910px;width:873px;height:254px;background:linear-gradient(180deg,var(--wood-dark),#1c130c 60%,#140d08)}
.tap-photo{left:140px;top:52px;width:165px;height:202px;
  background:
    radial-gradient(ellipse 20px 40px at 115px 145px,rgba(90,55,30,.95) 0%,rgba(0,0,0,0) 100%),
    linear-gradient(90deg,rgba(0,0,0,0) 34%,#8c8c8a 40%,#e6e6e2 46%,#7a7a78 52%,rgba(0,0,0,0) 58%),
    linear-gradient(180deg,#1c130c 0%,#1c130c 86%,#2b2520 92%,#0b0805 100%);}
.benefit-list{left:361px;top:92px;list-style:none;width:400px}
.benefit-list li{font-size:8.5px;line-height:16.5px;color:var(--cream);padding-left:23px;position:relative}
.benefit-list li::before{content:"";position:absolute;left:0;top:6px;width:13px;height:4px;border-radius:2px;background:var(--cream)}
.footer{left:0;top:1164px;width:873px;height:36px;background:var(--gold);text-align:center;line-height:36px;font-size:8.5px;color:#2a1d13}
</style>
</head>
<body>
<header>
  <div class="abs topbar"></div>
  <div class="abs phone">
    <span class="phone-icon"><svg width="9" height="9" viewBox="0 0 10 10"><path d="M2 1l2 2-1 1c.5 1.2 1.8 2.5 3 3l1-1 2 2-1.5 1.5C4 9 1 6 .5 2.5z" fill="#c9a06a"/></svg></span>
    (0123) 555 0198
  </div>
  <div class="abs follow">
    <span class="follow-label">Follow Us</span>
    <span class="social"></span><span class="social"></span><span class="social"></span><span class="social"></span>
  </div>
  <nav class="abs navbar">
    <a class="abs nav-item active" style="left:118px">Home</a>
    <span class="abs nav-dot" style="left:182px"></span>
    <a class="abs nav-item" style="left:224px">About Us</a>
    <span class="abs nav-dot" style="left:263px"></span>
    <a class="abs nav-item" style="left:319px">View Our Brews</a>
    <a class="abs nav-item" style="left:554px">Find A Store</a>
    <span class="abs nav-dot" style="left:600px"></span>
    <a class="abs nav-item" style="left:642px">Recipes</a>
    <span class="abs nav-dot" style="left:681px"></span>
    <a class="abs nav-item" style="left:728px">Contact Us</a>
  </nav>
  <div class="abs logo">
    <span class="logo-mark"></span>
    <span class="logo-name">Ferncastle<br>Coldbrew</span>
  </div>
</header>

<section class="abs hero" role="img" aria-label="Barista pouring cold brew coffee from a keg tap into a cup">
  <div class="abs hero-welcome">Welcome To</div>
  <div class="abs hero-title">Cold Brew Coffee</div>
  <svg class="abs arrow" style="left:75px" width="22" height="40" viewBox="0 0 22 40"><path d="M20 1L2 20l18 19" fill="none" stroke="#c8c2b8" stroke-width="1.5"/></svg>
  <svg class="abs arrow" style="left:776px" width="22" height="40" viewBox="0 0 22 40"><path d="M2 1l18 19L2 39" fill="none" stroke="#c8c2b8" stroke-width="1.5"/></svg>
</section>

<section class="abs features">
  <div class="abs feature" style="left:197px">
    <div class="feature-badge"><svg width="32" height="36" viewBox="0 0 32 36"><rect x="6" y="3" width="20" height="28" rx="2" fill="none" stroke="#c9a06a" stroke-width="2.5"/><path d="M11 11h10M11 16h10M11 21h10" stroke="#c9a06a" stroke-width="2"/></svg></div>
    <h3>Our Story</h3>
    <p>Lorem ipsum dolor sit amet,<br>consectetuer adipiscing elit, sed diam<br>nonummt dolo...[+]</p>
  </div>
  <div class="abs feature" style="left:437px">
    <div class="feature-badge"><svg width="38" height="32" viewBox="0 0 38 32"><path d="M7 6h20v10a10 10 0 0 1-20 0z" fill="none" stroke="#c9a06a" stroke-width="2.5"/><path d="M27 9h3a4 4 0 0 1 0 8h-3" fill="none" stroke="#c9a06a" stroke-width="2.5"/><ellipse cx="17" cy="28" rx="15" ry="3" fill="none" stroke="#c9a06a" stroke-width="2.5"/></svg></div>
    <h3>Recipes</h3>
    <p>Lorem ipsum dolor sit amet,<br>consectetuer adipiscing elit, sed diam<br>nonummt dolo...[+]</p>
  </div>
  <div class="abs feature" style="left:677px">
    <div class="feature-badge"><svg width="36" height="34" viewBox="0 0 36 34"><rect x="3" y="3" width="30" height="10" fill="#c9a06a"/><rect x="5" y="13" width="26" height="18" fill="none" stroke="#c9a06a" stroke-width="2.5"/><rect x="14" y="19" width="8" height="12" fill="#c9a06a"/></svg></div>
    <h3>Find A Store</h3>
    <p>Lorem ipsum dolor sit amet,<br>consectetuer adipiscing elit, sed diam<br>nonummt dolo...[+]</p>
  </div>
</section>

<section class="abs about">
  <h2 class="abs section-title" style="left:118px;top:22px">About <span>&nbsp;Cold Brew Coffee</span></h2>
  <div class="abs rule" style="left:118px;top:50px"></div>
  <p class="abs about-text">Lorem ipsum dolor sit amet, consectetuer adipiscing elit, sed diam nonummy nibh euismod tincidunt ut laoreet dolore magna aliquam erat volutpat. Ut wisi enim ad minim veniam, quis nostrud exerci tation ullamcorper suscipit lobortis nisl ut aliquip ex ea commodo consequat. Duis autem vel eum iriure dolor in hendrerit in vulputate velit esse molestie consequat, vel illum dolore eu feugiat nulla facilisis at vero eros et accumsan et iusto odio dignissim qui blandit praese\ugue duis dolore te feugait nulla facilisis.</p>
  <a class="abs read-more">Read More</a>
  <div class="abs about-photo" role="img" aria-label="Chef working in a busy café kitchen with shelves and a chalkboard menu"></div>
</section>

<section class="abs benefits">
  <div class="abs tap-photo" role="img" aria-label="Chrome keg tap tower pouring a glass of cold brew coffee"></div>
  <h2 class="abs section-title" style="left:361px;top:48px">Benefits of <span>Cold Brew Coffee</span></h2>
  <div class="abs rule" style="left:361px;top:76px"></div>
  <ul class="abs benefit-list">
    <li>Cold brew Coffee Can Improve Energy Levels and Make You Smarter</li>
    <li>The Caffeine Can Drastically Improve Physical Performance</li>
    <li>Cold brew Coffee is more than just black water. Many of the nutrients in the coffee beans do make it into the final drink.</li>
    <li>Cold brew Coffee May Lower Your Risk of Type II Diabetes</li>
    <li>Cold brew Coffee Without Milk &amp; Sugar</li>
    <li>Cold brew Coffee Can Fight Depression and Make You Happier</li>
    <li>Cold brew Coffee is The Biggest Source of Antioxidants in The Western Diet</li>
  </ul>
</section>

<footer class="abs footer">© 2016 Harrowgate Studio. All Rights Reserved.</footer>
</body>
</html>
```